Basic Letterhead Design

We need a Letterhead design. Our company is in the financial services industry. We are a small bank who lends money. I have uploaded an example our current letterhead design. We would like a new one.

```html
<!DOCTYPE html>
<html lang="en">
<head>
<meta charset="utf-8">
<title>Larkfield Lending Letterhead</title>
<link rel="stylesheet" href="https://fonts.googleapis.com/css2?family=Arimo:wght@400&family=Inter:wght@400;600&display=swap">
<style>
  :root {
    --backdrop: #e4e4e2;
    --paper: #f6f6f5;
    --brand-green: #21473a;
    --ink: #1a1a1a;
    --body-ink: #4a4a4a;
    --signature-tone: #d9d9d7;
  }
  * { margin: 0; padding: 0; box-sizing: border-box; }
  html, body {
    width: 1200px;
    height: 1141px;
    overflow: hidden;
    background: var(--backdrop);
  }
  .letterhead {
    position: absolute;
    left: 210px;
    top: 20px;
    width: 780px;
    height: 1100px;
    background: var(--paper);
    box-shadow: 0 2px 8px rgba(0,0,0,0.12);
  }
  .brand {
    position: absolute;
    left: 57px;
    top: 118px;
    display: flex;
    align-items: center;
    gap: 10px;
  }
  .brand-dot {
    width: 22px;
    height: 22px;
    border-radius: 50%;
    background: var(--brand-green);
  }
  .brand-name {
    font-family: "Inter", sans-serif;
    font-weight: 600;
    font-size: 22px;
    letter-spacing: 0.04em;
    color: var(--brand-green);
  }
  .sender {
    position: absolute;
    left: 555px;
    top: 92px;
    font-family: "Inter", sans-serif;
    font-size: 12.4px;
    line-height: 16.2px;
    color: var(--ink);
  }
  .sender-company, .sender-label { font-weight: 600; }
  .sender-acn { margin-top: 5px; }
  .salutation {
    position: absolute;
    left: 58px;
    top: 274px;
    font-family: "Arimo", sans-serif;
    font-size: 18.5px;
    color: var(--body-ink);
  }
  .letter-body {
    position: absolute;
    left: 58px;
    top: 332px;
    width: 665px;
    font-family: "Arimo", sans-serif;
    font-size: 11.2px;
    line-height: 16.6px;
    color: var(--body-ink);
    text-align: justify;
  }
  .letter-body p { margin-bottom: 16.6px; }
  .closing {
    position: absolute;
    left: 57px;
    top: 698px;
    font-family: "Arimo", sans-serif;
    font-size: 11.2px;
    color: var(--body-ink);
  }
  .signature {
    position: absolute;
    left: 54px;
    top: 740px;
    width: 226px;
    height: 62px;
    background: linear-gradient(90deg, var(--signature-tone), #ececea);
    border-radius: 3px;
  }
  .footer-band {
    position: absolute;
    left: 0;
    bottom: 0;
    width: 100%;
    height: 20px;
    background: var(--brand-green);
  }
</style>
</head>
<body>
  <main class="letterhead">
    <header>
      <div class="brand">
        <span class="brand-dot"></span>
        <span class="brand-name">LARKFIELD LENDING</span>
      </div>
      <address class="sender" style="font-style: normal;">
        <div class="sender-company">Larkfield Lending Pty Ltd</div>
        <div>47 Banksia Road</div>
        <div>Ellwood Nsw 2198</div>
        <div class="sender-acn"><span class="sender-label">ACN:</span> 512 083 671</div>
      </address>
    </header>

    <p class="salutation">Dear Mr. Harlow,</p>

    <section class="letter-body">
      <p>Lorem ipsum dolor sit amet, consectetur adipiscing elit. Donec orci purus, luctus vitae dignissim eu, iaculis sed purus. Vivamus faucibus, ipsum nec aliquet viverra, leo mauris condimentum ligula, sit amet sagittis enim ligula quis arcu. Nam egestas tortor id nisi porttitor mattis. In tortor ante, ultricies in suscipit a, tempus non massa. Vivamus et auctor mi. Fusce vel massa nulla. Phasellus nec eros mauris, et scelerisque orci.</p>
      <p>Donec malesuada orci vitae nulla accumsan porta a id massa. Quisque accumsan iaculis magna sit amet fringilla. Maecenas consequat, magna eget tincidunt semper, odio nibh rutrum mi, id feugiat ante nisi eu risus. Vestibulum nunc orci, rhoncus a placerat in, ultricies in mi. Cras mattis varius eros, vel fringilla nisi suscipit eget. Quisque scelerisque sagittis nulla at porttitor.</p>
      <p>Sed id augue vitae urna euismod commodo aliquet a quam. Pellentesque arcu velit, cursus et malesuada ut, consequat et diam. Nullam erat sem, rhoncus id ullamcorper vitae, rhoncus et arcu. In ultricies ultricies nulla, ut rutrum nisi iaculis at. Donec eu magna a metus ornare faucibus. Fusce aliquet faucibus ultricies. Morbi semper, est id tincidunt gravida, sem arcu adipiscing lacus, ac bibendum nulla leo eu purus. Quisque nec diam sed risus consectetur a ccumsan quis quis nibh. Vestibulum id purus lorem.</p>
      <p>It is a long established fact that a reader will be distracted by the readable content of a page when looking at its layout. The point of using Lorem Ipsum is that it has a more-or-less normal distribution of letters, as opposed to using 'Content here, content here', making it look like readable English. Many desktop publishing packages</p>
      <p>ada ut, consequat et diam. Nullam erat sem, rhoncus id ullamcorper vitae, rhoncus et arcu. In ultricies ultricies nulla, ut rutrum nisi iaculis at. Donec eu magna a metus ornare faucibus. Fusce aliquet faucibus ultricies. Morbi semper,</p>
    </section>

    <p class="closing">Sincerely,</p>
    <div class="signature" role="img" aria-label="Handwritten signature of the sender"></div>

    <div class="footer-band"></div>
  </main>
</body>
</html>
```